Infographic for Labor Trends - Supply Chain Theme

Looking to polish this slide up to look professional enough to share with the Board of Directors. The focus is Supply Chain Labor (Warehousing and transportation) Need to have a theme around Supply Chain workforce. Needs to be formatted for wide screen PowerPoint

```html
<!DOCTYPE html>
<html lang="en">
<head>
<meta charset="utf-8">
<title>Supply Chain Job Market Remains Tight</title>
<link href="https://fonts.googleapis.com/css2?family=Oswald:wght@600;700&family=Roboto:wght@400;500;700;900&family=Roboto+Condensed:wght@700&display=swap" rel="stylesheet">
<style>
:root{
  --navy:#1d4f9c;
  --navy-dark:#173f80;
  --sky:#3ba7df;
  --ring:#bfe1f5;
  --ink:#1e1e1e;
  --green:#55b24a;
  --green-text:#3f9a36;
  --blue-bar:#1f4e96;
  --orange:#d86a22;
  --hosp:#213f95;
  --load:#d63f7c;
  --logi:#2c8a6d;
  --retail:#d3a23c;
  --grid:#dcdcdc;
  --white:#ffffff;
}
*{box-sizing:border-box;margin:0;padding:0}
html,body{width:1200px;height:675px;overflow:hidden;background:var(--white)}
body{font-family:"Roboto",Arial,sans-serif;color:var(--ink);position:relative}
.header{position:absolute;left:0;top:0;width:1200px;height:90px;background:var(--navy)}
.header h1{position:absolute;left:22px;top:10px;font-family:"Oswald",Impact,sans-serif;font-weight:700;font-size:48px;line-height:70px;color:var(--white);letter-spacing:.3px;white-space:nowrap}
.intro{position:absolute;top:90px;left:0;width:1200px;height:134px;background:var(--white)}
.badge{position:absolute;top:14px;width:100px;height:100px}
.point-text{position:absolute;top:20px;font-size:15px;line-height:19.5px}
.point-text strong{color:var(--navy);font-weight:700}
.worker-art{position:absolute;left:1060px;top:14px;width:125px;height:205px;border-radius:8px;background:linear-gradient(160deg,#f2b266,#e07b3d 60%,#c8c8c8)}
.stage{position:absolute;left:0;top:224px;width:1200px;height:451px;background:var(--sky)}
.panel{position:absolute;background:var(--white)}
.bars-panel{left:17px;top:237px;width:560px;height:426px}
.panel h2{font-family:"Roboto Condensed",Arial,sans-serif;font-weight:700;font-size:15px;text-align:center;color:var(--ink)}
.bars-panel h2{position:absolute;top:9px;left:0;width:100%;font-size:16px}
.bars-panel h3{position:absolute;top:36px;left:0;width:100%;text-align:center;font-family:"Roboto Condensed",Arial,sans-serif;font-size:12px;font-weight:700}
.group-label{position:absolute;left:116px;font-family:"Roboto Condensed",Arial,sans-serif;font-weight:700;font-size:12px}
.better{color:var(--green-text)} .similar{color:var(--blue-bar)} .worse{color:var(--orange)}
.bar-row{position:absolute;left:0;height:19px;display:flex;align-items:center}
.bar-row .name{width:116px;text-align:right;font-family:"Roboto Condensed",Arial,sans-serif;font-size:7.5px;font-weight:700;padding-right:6px;text-transform:uppercase}
.bar-row .bar{height:19px}
.bar-row .val{font-weight:700;font-size:16px;margin-left:6px}
.bar-green{background:var(--green)} .bar-blue{background:var(--blue-bar)} .bar-orange{background:var(--orange)}
.truck-art{position:absolute;left:296px;top:290px;width:244px;height:126px;border-radius:6px;background:linear-gradient(180deg,#d7e3ee,#f2a33a 70%,#5a6270)}
.trend-panel{left:591px;top:237px;width:593px;height:207px}
.incentive-panel{left:591px;top:456px;width:593px;height:207px}
.panel-title{position:absolute;top:9px;left:0;width:100%}
.side-icon{position:absolute;left:55px}
.side-text{position:absolute;left:16px;width:155px;text-align:center;font-size:15px;line-height:19px}
.legend{position:absolute;top:34px;left:198px;display:flex;gap:14px;font-family:"Roboto Condensed",Arial,sans-serif;font-size:8.5px;font-weight:700}
.legend span{display:flex;align-items:center;gap:4px}
.legend i{display:inline-block;width:10px;height:10px}
.chart{position:absolute}
.chart text{font-family:"Roboto",Arial,sans-serif;font-size:7px;fill:#555}
</style>
</head>
<body>
<header class="header"><h1>SUPPLY CHAIN JOB MARKET REMAINS TIGHT</h1></header>

<section class="intro">
  <svg class="badge" style="left:20px" viewBox="0 0 104 104"><circle cx="52" cy="52" r="50" fill="var(--ring)"/><circle cx="52" cy="52" r="42" fill="var(--navy)"/><circle cx="47" cy="47" r="16" fill="none" stroke="#fff" stroke-width="4"/><line x1="58" y1="58" x2="70" y2="70" stroke="#fff" stroke-width="6" stroke-linecap="round"/><circle cx="47" cy="42" r="5" fill="#fff"/><path d="M38 55a9 8 0 0 1 18 0z" fill="#fff"/></svg>
  <p class="point-text" style="left:133px;width:185px">We continue to see pressure and struggle to attract the talent needed <strong>to meet staffing demands</strong> in multiple markets.</p>

  <svg class="badge" style="left:333px" viewBox="0 0 104 104"><circle cx="52" cy="52" r="50" fill="var(--ring)"/><circle cx="52" cy="52" r="42" fill="var(--navy)"/><path d="M52 24 66 44H59L71 60H63L75 74H29L41 60H33L45 44H38Z" fill="#fff"/><rect x="48" y="74" width="8" height="8" fill="#fff"/></svg>
  <p class="point-text" style="left:450px;width:172px">Wage inflation in the industry continues and is amplified <strong>lack of talent to cover demand for the holiday season cycle.</strong></p>

  <svg class="badge" style="left:640px" viewBox="0 0 104 104"><circle cx="52" cy="52" r="50" fill="var(--ring)"/><circle cx="52" cy="52" r="42" fill="var(--navy)"/><rect x="30" y="32" width="36" height="34" rx="2" fill="#fff"/><rect x="30" y="32" width="36" height="9" fill="#cfe3f3"/><circle cx="66" cy="64" r="12" fill="var(--navy)" stroke="#fff" stroke-width="3"/><path d="M66 58v7h5" stroke="#fff" stroke-width="2.5" fill="none"/></svg>
  <p class="point-text" style="left:756px;width:235px">We expect <strong>demand to remain extremely high through 2022 period</strong> due to the amount of backlog freight at the ports and missed Holiday placement of goods.</p>
</section>
<div class="worker-art" role="img" aria-label="Illustration of a warehouse worker pushing a hand truck stacked with boxes"></div>

<div class="stage"></div>

<section class="panel bars-panel">
  <h2>SOME SECTORS ARE BOOMING WHILE OTHERS LAG</h2>
  <h3>% CHANGE IN US JOB POSTINGS SINCE FEB 1, 2020, SEASONALLY ADJUSTED TO OCT 8,2021</h3>
  <div class="group-label better" style="top:62px">Better Than Economy Average</div>
  <div class="bar-row" style="top:78px"><span class="name">Human Resources</span><span class="bar bar-green" style="width:380px"></span><span class="val">92.9%</span></div>
  <div class="bar-row" style="top:102px"><span class="name">Production &amp; Manufacturing</span><span class="bar bar-green" style="width:368px"></span><span class="val">89.9%</span></div>
  <div class="bar-row" style="top:126px"><span class="name">Loading &amp; Stocking</span><span class="bar bar-green" style="width:366px"></span><span class="val">89.4%</span></div>
  <div class="bar-row" style="top:150px"><span class="name">Pharmacy</span><span class="bar bar-green" style="width:364px"></span><span class="val">89.0%</span></div>
  <div class="group-label similar" style="top:176px">Similar to Economy Average</div>
  <div class="bar-row" style="top:196px"><span class="name">Driving</span><span class="bar bar-blue" style="width:210px"></span><span class="val">51.4%</span></div>
  <div class="bar-row" style="top:219px"><span class="name">Childcare</span><span class="bar bar-blue" style="width:207px"></span><span class="val">50.6%</span></div>
  <div class="bar-row" style="top:242px"><span class="name">Arts &amp; Entertainment</span><span class="bar bar-blue" style="width:182px"></span><span class="val">44.4%</span></div>
  <div class="bar-row" style="top:265px"><span class="name">Food Preparation &amp; Service</span><span class="bar bar-blue" style="width:158px"></span><span class="val">38.7%</span></div>
  <div class="group-label worse" style="top:299px">Worse Than Economy Average</div>
  <div class="bar-row" style="top:315px"><span class="name">Sales</span><span class="bar bar-orange" style="width:82px"></span><span class="val">20.0%</span></div>
  <div class="bar-row" style="top:338px"><span class="name">Hospitality &amp; Tourism</span><span class="bar bar-orange" style="width:76px"></span><span class="val">18.6%</span></div>
  <div class="bar-row" style="top:362px"><span class="name">Sports</span><span class="bar bar-orange" style="width:54px"></span><span class="val">13.2%</span></div>
  <div class="bar-row" style="top:386px"><span class="name" style="width:100px">Beauty &amp; Wellness</span><span class="bar bar-orange" style="width:16px"></span><span class="val">-3.8%</span></div>
  <div class="truck-art" role="img" aria-label="Illustration of a delivery truck with a worker carrying boxes"></div>
</section>

<section class="panel trend-panel">
  <h2 class="panel-title">% CHANGE IN JOB POSTINGS SINCE FEB 1, 2020, SEASONALLY ADJUSTED TO OCT 8,2021</h2>
  <div class="legend">
    <span><i style="background:var(--hosp)"></i>HOSPITALITY &amp; TOURISM</span>
    <span><i style="background:var(--load)"></i>LOADING &amp; STOCKING</span>
    <span><i style="background:var(--logi)"></i>LOGISTIC SUPPORT</span>
    <span><i style="background:var(--retail)"></i>RETAIL</span>
  </div>
  <svg class="side-icon" style="top:48px" width="80" height="80" viewBox="0 0 80 80"><circle cx="40" cy="40" r="38" fill="var(--navy)"/><rect x="24" y="22" width="32" height="36" rx="3" fill="none" stroke="#fff" stroke-width="3"/><text x="40" y="45" text-anchor="middle" font-family="Roboto Condensed,Arial,sans-serif" font-weight="700" font-size="11" fill="#fff">JOBS</text></svg>
  <p class="side-text" style="top:133px">Total Job Postings on Jobsly by Occupational Sector</p>
  <svg class="chart" style="left:192px;top:50px" width="395" height="155" viewBox="0 0 430 168" preserveAspectRatio="none">
    <g stroke="var(--grid)" stroke-width=".6">
      <line x1="40" y1="5" x2="425" y2="5"/><line x1="40" y1="17.8" x2="425" y2="17.8"/><line x1="40" y1="30.6" x2="425" y2="30.6"/><line x1="40" y1="43.3" x2="425" y2="43.3"/><line x1="40" y1="56.1" x2="425" y2="56.1"/><line x1="40" y1="68.9" x2="425" y2="68.9"/><line x1="40" y1="81.7" x2="425" y2="81.7"/><line x1="40" y1="94.5" x2="425" y2="94.5"/><line x1="40" y1="107.3" x2="425" y2="107.3"/><line x1="40" y1="120" x2="425" y2="120"/>
    </g>
    <g text-anchor="end">
      <text x="34" y="8">100%</text><text x="34" y="21">80%</text><text x="34" y="33">60%</text><text x="34" y="46">40%</text><text x="34" y="59">20%</text><text x="34" y="72">0%</text><text x="34" y="85">-20%</text><text x="34" y="97">-40%</text><text x="34" y="110">-60%</text><text x="34" y="123">-80%</text>
    </g>
    <g text-anchor="end">
      <text transform="translate(44,130) rotate(-50)">Feb 1 '20</text><text transform="translate(79,130) rotate(-50)">Apr 1 '20</text><text transform="translate(117,130) rotate(-50)">Jun 1 '20</text><text transform="translate(156,130) rotate(-50)">Aug 1 '20</text><text transform="translate(194,130) rotate(-50)">Oct 1 '20</text><text transform="translate(233,130) rotate(-50)">Dec 1 '20</text><text transform="translate(271,130) rotate(-50)">Feb 1 '21</text><text transform="translate(310,130) rotate(-50)">Apr 1 '21</text><text transform="translate(348,130) rotate(-50)">Jun 1 '21</text><text transform="translate(387,130) rotate(-50)">Aug 1 '21</text><text transform="translate(425,130) rotate(-50)">Oct 1 '21</text>
    </g>
    <g fill="none" stroke-width="1.8" stroke-linejoin="round">
      <polyline stroke="var(--retail)" points="40,68.9 59,72.1 79,97.7 98,97.7 117,91.3 136,81.7 156,75.3 175,72.1 194,68.9 213,68.9 233,68.9 252,65.7 271,62.5 290,59.3 310,56.1 329,52.9 348,49.7 367,49.7 387,46.5 406,46.5 425,43.3"/>
      <polyline stroke="var(--logi)" points="40,68.9 59,72.1 79,94.5 98,94.5 117,88.1 136,81.7 156,75.3 175,72.1 194,68.9 213,68.9 233,68.9 252,65.7 271,59.3 290,56.1 310,49.7 329,43.3 348,40.1 367,33.8 387,30.6 406,27.4 425,24.2"/>
      <polyline stroke="var(--load)" points="40,68.9 59,72.1 79,91.3 98,88.1 117,75.3 136,62.5 156,56.1 175,49.7 194,46.5 213,49.7 233,52.9 252,49.7 271,46.5 290,43.3 310,37 329,30.6 348,27.4 367,24.2 387,21 406,17.8 425,11.4"/>
      <polyline stroke="var(--hosp)" points="40,68.9 59,75.3 79,104.1 98,107.3 117,104.1 136,100.9 156,97.7 175,97.7 194,95.7 213,94.5 233,94.5 252,93.2 271,88.1 290,84.9 310,78.5 329,72.1 348,68.9 367,65.7 387,62.5 406,62.5 425,57.4"/>
    </g>
  </svg>
</section>

<section class="panel incentive-panel">
  <h2 class="panel-title">SHARE OF JOB POSTINGS THAT ADVERTISE HIRING INCENTIVES THROUGH JULY 16, 2021</h2>
  <svg class="side-icon" style="top:45px" width="80" height="80" viewBox="0 0 80 80"><circle cx="40" cy="40" r="38" fill="var(--navy)"/><path d="M22 34h8l18-10v32l-18-10h-8z" fill="#fff"/><rect x="28" y="46" width="6" height="12" fill="#fff"/><path d="M53 32q5 8 0 16M57 28q9 12 0 24" stroke="#fff" stroke-width="2.5" fill="none"/></svg>
  <p class="side-text" style="top:130px">More postings are advertising hiring incentives</p>
  <svg class="chart" style="left:186px;top:40px" width="400" height="165" viewBox="0 0 400 165" preserveAspectRatio="none">
    <g stroke="var(--grid)" stroke-width=".6">
      <line x1="30" y1="8" x2="385" y2="8"/><line x1="30" y1="32" x2="385" y2="32"/><line x1="30" y1="56" x2="385" y2="56"/><line x1="30" y1="80" x2="385" y2="80"/><line x1="30" y1="104" x2="385" y2="104"/><line x1="30" y1="128" x2="385" y2="128"/>
    </g>
    <g text-anchor="end">
      <text x="24" y="11">5%</text><text x="24" y="35">4%</text><text x="24" y="59">3%</text><text x="24" y="83">2%</text><text x="24" y="107">1%</text><text x="24" y="131">0%</text>
    </g>
    <g text-anchor="middle" style="font-weight:700">
      <text x="36" y="146" style="font-size:8px">Jul 2020</text><text x="118" y="146" style="font-size:8px">Oct 2020</text><text x="205" y="146" style="font-size:8px">Jan 2021</text><text x="290" y="146" style="font-size:8px">Apr 2021</text><text x="370" y="146" style="font-size:8px">Jul 2021</text>
    </g>
    <polyline fill="none" stroke="var(--navy-dark)" stroke-width="2" stroke-linejoin="round" points="30,85 50,82 80,79 120,77 160,73 190,66 205,64 215,68 240,67 270,65 300,60 330,48 350,38 365,28 380,22"/>
  </svg>
</section>
</body>
</html>
```